Verdant Ledger - Paid Surveys publisher portal

• Homepage
• Blank Sub Page (Where content goes in between the header/footer)
• Publisher Application Page, complete with Form
• Survey Wall page

Sites that are in a similar vertical that have interesting designs:
mobrivex.com
tandulo.com
vorql.com
pim.ox

This is a business-to-business site, and needs to have this type of feel to it. Focus on generating revenue, offer completion, paid surveys is the market.

Format: HTML/CSS

Link to current version of application, and form:
https://quorbit.travenlo.com
https://quorbit.travenlo.com/apply
https://quorbit.travenlo.com/panel/4/mirvak_user

Please note that we are changing the brand of this project, the name will be determined shortly but everything else remains. It will likely be Verdant Ledger instead of Quorbit. We will confirm.

Industry/Entity Type

Market Research

Coding

Coded - Design and coding required

Number of Pages Required

4 page

Font styles to use
Sans Serif

Colors

Designer to choose colors to be used in the design.

```html
<!DOCTYPE html>
<html lang="en">
<head>
<meta charset="utf-8">
<title>Verdant Ledger – Sub Page</title>
<link rel="stylesheet" href="https://fonts.googleapis.com/css2?family=Roboto:wght@300;400;500;700&family=Roboto+Condensed:wght@400;700&display=swap">
<style>
  :root {
    --header-bg: #0b0b0b;
    --mark-grey: #5a5f68;
    --white: #ffffff;
    --heading: #1d1d1d;
    --body-dark: #1f1f1f;
    --body-muted: #7a7a7a;
    --footer-bg: #262626;
    --footer-text: #9a9a9a;
    --hero-a: #59616c;
    --hero-b: #8c939c;
  }
  * { box-sizing: border-box; margin: 0; padding: 0; }
  html, body { width: 768px; height: 1200px; overflow: hidden; background: var(--white); }
  body { position: relative; font-family: "Roboto", Arial, sans-serif; color: var(--body-dark); }

  .site-header { position: absolute; left: 0; top: 0; width: 768px; height: 55px; background: var(--header-bg); }
  .brand { position: absolute; left: 115px; top: 12px; display: flex; align-items: center; gap: 7px; }
  .brand-mark { width: 28px; height: 28px; background: var(--mark-grey); }
  .brand-name { color: var(--white); font-family: "Roboto Condensed", Arial, sans-serif; font-weight: 700; font-size: 12px; line-height: 13px; width: 60px; text-transform: uppercase; }
  .main-nav { position: absolute; top: 21px; font-family: "Roboto Condensed", Arial, sans-serif; font-weight: 700; font-size: 8.5px; color: var(--white); text-transform: uppercase; letter-spacing: .2px; }
  .nav-home { left: 298px; }
  .nav-publisher { left: 343px; }
  .nav-survey { left: 449px; }
  .nav-active-bar { position: absolute; left: 294px; top: 52px; width: 30px; height: 3px; background: var(--white); }
  .nav-account { position: absolute; left: 566px; top: 20px; display: flex; align-items: center; gap: 5px; font-family: "Roboto Condensed", Arial, sans-serif; font-size: 8.5px; color: var(--white); }
  .nav-search { position: absolute; left: 649px; top: 20px; }

  .page-hero { position: absolute; left: 0; top: 55px; width: 768px; height: 121px; background: linear-gradient(100deg, var(--hero-a), var(--hero-b) 45%, var(--hero-a)); }
  .page-title { position: absolute; left: 0; top: 98px; width: 768px; text-align: center; font-weight: 300; font-size: 24.5px; color: var(--white); }

  .section-heading { position: absolute; font-weight: 300; color: var(--heading); font-size: 23.5px; letter-spacing: .3px; }
  .copy { position: absolute; font-size: 9.3px; line-height: 14.6px; text-align: justify; }
  .copy p + p { margin-top: 6px; }
  .copy .lead { color: #111; }
  .copy .muted { color: var(--body-muted); }
  .copy .narrow { width: 262px; text-align: left; }

  .media { position: absolute; }

  .site-footer { position: absolute; left: 0; top: 1098px; width: 768px; height: 102px; background: var(--footer-bg); }
  .to-top { position: absolute; left: 373px; top: 1087px; width: 22px; height: 22px; border-radius: 50%; background: var(--header-bg); display: flex; align-items: center; justify-content: center; }
  .footer-links { position: absolute; left: 0; top: 1122px; width: 768px; text-align: center; font-family: "Roboto Condensed", Arial, sans-serif; font-size: 8px; color: var(--footer-text); }
  .footer-social { position: absolute; left: 375px; top: 1148px; display: flex; gap: 10px; }
  .footer-social span { width: 7px; height: 7px; border-radius: 50%; background: var(--white); }
  .copyright { position: absolute; left: 0; top: 1174px; width: 768px; text-align: center; font-family: "Roboto Condensed", Arial, sans-serif; font-size: 7.5px; color: var(--footer-text); }
</style>
</head>
<body>
  <header class="site-header">
    <div class="brand"><span class="brand-mark"></span><span class="brand-name">Verdant Ledger</span></div>
    <nav>
      <span class="main-nav nav-home">Home &#8964;</span>
      <span class="main-nav nav-publisher">Publisher Application</span>
      <span class="main-nav nav-survey">Survey</span>
      <span class="nav-active-bar"></span>
      <span class="nav-account">
        <svg width="8" height="9" viewBox="0 0 8 9"><circle cx="4" cy="2.3" r="2.2" fill="#fff"/><path d="M0 9c0-3 1.8-4.4 4-4.4S8 6 8 9z" fill="#fff"/></svg>
        Login / Signup &#8964;
      </span>
      <span class="nav-search">
        <svg width="9" height="9" viewBox="0 0 9 9"><circle cx="3.7" cy="3.7" r="2.8" fill="none" stroke="#fff" stroke-width="1.4"/><path d="M5.8 5.8 8.4 8.4" stroke="#fff" stroke-width="1.6"/></svg>
      </span>
    </nav>
  </header>

  <div class="page-hero" role="img" aria-label="Photo of a team working around a meeting table, darkened"></div>
  <h1 class="page-title">Rerum necessitatibus saepe eveniet</h1>

  <h2 class="section-heading" style="left:110px; top:215px;">Omnis voluptas assum</h2>
  <div class="copy" style="left:110px; top:258px; width:308px;">
    <p class="lead">Nemo enim ipsam voluptatem quia voluptas sit &nbsp;aut odit aut sed quia ration voluptatem quis nostrum ullam corporis. Nam libero tempore, cum soluta nobis est eligendi optio cumque nihil impedit quo minus id quod maxime placeat facere possimus.</p>
    <p class="muted" style="margin-top:11px;">Nemo enim ipsam voluptatem quia voluptas sit &nbsp;aut odit aut sed quia ratione voluptatem quis nostrum ullam corporis. Nam libero tempore, cum soluta nobis est eligendi optio cumque nihil impedit quo minus id quod maxime placeat facere possimus.</p>
    <p class="muted" style="margin-top:9px; text-align:left;">Quis autem vel eum iure reprehenderit qui in ea voluptate velit esse quam nihil molestiae consequatur, vel illum qui dolorem eum fugiat sapiente voluptates repudiandae sint et molestiae non recusandae.</p>
  </div>
  <div class="media" style="left:437px; top:259px; width:220px; height:178px; background:linear-gradient(160deg,#e4e8ee,#b9c3cf 55%,#8e9aa8);" role="img" aria-label="Video still of a business team meeting in a bright office"></div>

  <div class="media" style="left:110px; top:488px; width:266px; height:297px; background:linear-gradient(180deg,#ffffff,#eef0f3 40%,#dfe2e7);" role="img" aria-label="Photo of two smiling business professionals standing with arms crossed"></div>
  <h2 class="section-heading" style="left:392px; top:513px;">Necessitatibus saepe</h2>
  <div class="copy" style="left:391px; top:558px; width:266px;">
    <p>Neque porro quisquam est, qui dolorem ipsum quia dolor sit amet, consectetur, adipisci velit, sed quia non numquam eius modi tempora incidunt ut labore et dolore magnam aliquam quaerat voluptatem. Ut enim ad minima veniam, quis nostrum exercitationem ullam corporis suscipit laboriosam, nisi ut aliquid ex ea commodi consequatur</p>
    <p class="narrow">Ullamco laboris nisi ut aliquip ex ea commodo consequat. Duis aute irure dolor in reprehenderit in voluptate velit esse cillum dolore eu fugiat nulla pariatur. Excepteur sint occaecat cupidatat non proident, sunt in culpa qui officia deserunt mollit anim id est laborum.</p>
    <p class="narrow">Ullamco laboris nisi ut aliquip ex ea commodo consequat. Duis aute irure dolor in reprehenderit in voluptate velit esse cillum dolore eu fugiat nulla pariatur. Excepteur sint occaecat cupidatat non proident, sunt in culpa qui officia deserunt mollit anim id est laborum.</p>
  </div>

  <div class="copy" style="left:111px; top:846px; width:546px;">
    <p>Nam libero tempore, cum soluta nobis est eligendi optio cumque nihil impedit quo minus id quod maxime placeat facere possimus, omnis voluptas assumenda est, omnis dolor repellendus. Temporibus autem quibusdam et aut officiis debitis aut rerum necessitatibus.Saepe eveniet ut et voluptates repudiandae sint et molestiae non recusandae. Itaque earum rerum hic tenetur a sapiente delectus,</p>
    <p>Neque porro quisquam est, qui dolorem ipsum quia dolor sit amet, consectetur, adipisci velit, sed quia non numquam eius modi tempora incidunt ut labore et dolore magnam aliquam quaerat voluptatem. Ut enim ad minima veniam, quis nostrum exercitationem ullam corporis suscipit laboriosam, nisi ut aliquid ex ea commodi consequatur blanditiis praesentium voluptatum deleniti atque corrupti quos dolores et quas molestias excepturi sint occaecati cupiditate non provident, similique sunt in culpa qui officia deserunt mollitia animi, id est laborum et dolorum fuga. Et harum quidem rerum facilis est et expedita distinctio.</p>
    <p style="margin-top:14px;">Nam libero tempore, cum soluta nobis est eligendi optio cumque nihil impedit quo minus id quod maxime placeat facere possimus, omnis voluptas assumenda est, omnis dolor repellendus. Temporibus autem quibusdam et aut officiis debitis aut rerum necessitatibus saepe eveniet ut et voluptates repudiandae sint et molestiae non recusandae. Itaque earum rerum hic tenetur a sapiente delectus, ut aut reiciendis voluptatibus maiores alias consequatur aut perferendis doloribus asperiores repellat.</p>
  </div>

  <footer class="site-footer"></footer>
  <div class="to-top"><svg width="9" height="6" viewBox="0 0 9 6"><path d="M1 5 4.5 1.5 8 5" fill="none" stroke="#fff" stroke-width="1.5"/></svg></div>
  <div class="footer-links">Home | Publisher | Survey</div>
  <div class="footer-social"><span></span><span></span></div>
  <div class="copyright">©Copyright information here</div>
</body>
</html>
```